Business Card Design - Law Firm

I need a business card design. I have attached a picture of the law firm's website and logo. The business card design should be consistent with those pictures. There should be a place for the employee name, employee job title, telephone number, facsimile number, address, website url, and email address for each employee.
Industry/Entity Type
Business

```html
<!DOCTYPE html>
<html lang="en">
<head>
<meta charset="utf-8">
<title>Marlowe Law – Business Card</title>
<link rel="stylesheet" href="https://fonts.googleapis.com/css2?family=Tinos:ital,wght@0,400;1,700&family=Arimo:wght@400&display=swap">
<style>
  :root {
    --stage: #ebe6de;
    --card-white: #ffffff;
    --card-grey: #e4e4e6;
    --orange: #d9692e;
    --sand: #dccaa5;
    --gold: #a88a4c;
    --ink: #1e1e1e;
    --dark-mark: #1b1b1b;
    --photo-sky: #c9d3cb;
    --photo-sea: #7f9f98;
    --photo-sand: #d8c7ad;
  }
  * { margin: 0; padding: 0; box-sizing: border-box; }
  html, body {
    width: 1200px; height: 1106px; overflow: hidden;
    background: var(--stage);
  }
  .canvas { position: relative; width: 1200px; height: 1106px; }
  .card {
    position: absolute; width: 838px; height: 478px;
    border-radius: 26px; overflow: hidden;
    box-shadow: 0 8px 18px rgba(0,0,0,0.25);
  }
  .card svg.card-art { position: absolute; inset: 0; }
  .card-front { left: 249px; top: 41px; }
  .card-back { left: 91px; top: 556px; }

  .brand {
    position: absolute; display: flex; align-items: center;
  }
  .brand-square { background: var(--dark-mark); }
  .brand-name {
    font-family: "Tinos", serif; font-weight: 400; color: var(--gold);
    white-space: nowrap; line-height: 1;
  }
  .card-front .brand { left: 540px; top: 404px; gap: 16px; }
  .card-front .brand-square { width: 44px; height: 44px; }
  .card-front .brand-name { font-size: 36px; }

  .card-back .brand { left: 62px; top: 72px; gap: 26px; }
  .card-back .brand-square { width: 76px; height: 76px; }
  .card-back .brand-name { font-size: 52px; }

  .employee {
    position: absolute; right: 50px; top: 76px; text-align: right;
  }
  .employee-name {
    font-family: "Tinos", serif; font-style: italic; font-weight: 700;
    font-size: 25px; color: var(--gold); line-height: 1.1;
  }
  .employee-title {
    font-family: "Arimo", sans-serif; font-size: 19px; color: var(--ink);
    margin-top: 4px;
  }
  .contact {
    position: absolute; top: 228px; list-style: none;
    font-family: "Arimo", sans-serif; font-size: 20px; color: var(--ink);
  }
  .contact li { display: flex; align-items: flex-start; gap: 12px; line-height: 27px; }
  .contact svg { flex: none; width: 18px; height: 18px; margin-top: 4px; }
  .contact-left { left: 122px; }
  .contact-right { left: 520px; }
</style>
</head>
<body>
<main class="canvas">

  <!-- Front side -->
  <section class="card card-front" aria-label="Card front">
    <svg class="card-art" width="838" height="478" viewBox="0 0 838 478" aria-hidden="false">
      <defs>
        <linearGradient id="photoTone" x1="0" y1="0" x2="1" y2="0">
          <stop offset="0" stop-color="#ffffff"/>
          <stop offset="0.12" stop-color="#f3efe9"/>
          <stop offset="0.35" stop-color="var(--photo-sand)"/>
          <stop offset="0.7" stop-color="var(--photo-sea)"/>
          <stop offset="1" stop-color="var(--photo-sky)"/>
        </linearGradient>
      </defs>
      <rect class="sand-base" width="838" height="478" fill="var(--sand)"/>
      <path class="photo-area" role="img" aria-label="Photo of a smiling family walking hand in hand along a beach"
            d="M0,0 H838 V300 C640,370 430,420 0,280 Z" fill="url(#photoTone)"/>
      <path class="swoop" d="M0,276 C200,360 420,440 838,300 C560,425 300,435 0,318 Z" fill="var(--orange)"/>
    </svg>
    <div class="brand">
      <span class="brand-square"></span>
      <span class="brand-name">Marlowe Law</span>
    </div>
  </section>

  <!-- Back side -->
  <section class="card card-back" aria-label="Card back">
    <svg class="card-art" width="838" height="478" viewBox="0 0 838 478">
      <defs>
        <linearGradient id="cardSheen" x1="0" y1="0" x2="0" y2="1">
          <stop offset="0" stop-color="var(--card-grey)"/>
          <stop offset="0.45" stop-color="var(--card-white)"/>
          <stop offset="1" stop-color="var(--card-grey)"/>
        </linearGradient>
      </defs>
      <rect class="paper" width="838" height="478" fill="url(#cardSheen)"/>
      <path class="sand-band" d="M0,392 C240,478 560,470 838,358 V478 H0 Z" fill="var(--sand)"/>
      <path class="swoop" d="M0,316 C180,392 430,450 838,350 C560,462 250,470 0,376 Z" fill="var(--orange)"/>
      <path class="tab-arrow" d="M838,88 L838,122 L805,106 Z" fill="var(--orange)"/>
    </svg>

    <div class="brand">
      <span class="brand-square"></span>
      <span class="brand-name">Marlowe Law</span>
    </div>

    <div class="employee">
      <p class="employee-name">Mr. Ansel Marlowe</p>
      <p class="employee-title">Chief Executive</p>
    </div>

    <ul class="contact contact-left">
      <li>
        <svg viewBox="0 0 18 18" aria-label="Email"><rect x="1.5" y="4" width="15" height="10" fill="none" stroke="var(--orange)" stroke-width="2"/><path d="M1.5,4 L9,10 L16.5,4" fill="none" stroke="var(--orange)" stroke-width="2"/></svg>
        <span>info@marlowelaw.com</span>
      </li>
      <li>
        <svg viewBox="0 0 18 18" aria-label="Website"><circle cx="9" cy="9" r="7" fill="none" stroke="var(--orange)" stroke-width="2"/><path d="M2,9 H16 M9,2 C5,6 5,12 9,16 M9,2 C13,6 13,12 9,16" fill="none" stroke="var(--orange)" stroke-width="1.5"/></svg>
        <span>www.marlowelaw.com</span>
      </li>
      <li>
        <svg viewBox="0 0 18 18" aria-label="Address"><path d="M1.5,9 L9,2 L16.5,9 M4,8 V16 H14 V8" fill="none" stroke="var(--orange)" stroke-width="2"/><rect x="7.5" y="11" width="3" height="5" fill="var(--orange)"/></svg>
        <span>22,23,24, XXXX Floor,<br>XXXX Centre, City, Country</span>
      </li>
    </ul>

    <ul class="contact contact-right">
      <li>
        <svg viewBox="0 0 18 18" aria-label="Telephone"><circle cx="9" cy="9" r="7.5" fill="none" stroke="var(--orange)" stroke-width="2"/><path d="M7,5 C5,8 7,12 11,13 L12,11 L10,10 L9,11 C8,10 7.5,9 7.5,8 L8.5,7 Z" fill="var(--orange)"/></svg>
        <span>(555) 014 220 318</span>
      </li>
      <li>
        <svg viewBox="0 0 18 18" aria-label="Fax"><rect x="5" y="2" width="8" height="4" fill="none" stroke="var(--orange)" stroke-width="1.6"/><rect x="1.5" y="6" width="15" height="7" rx="1.5" fill="var(--orange)"/><rect x="5" y="11" width="8" height="5" fill="#fff" stroke="var(--orange)" stroke-width="1.6"/></svg>
        <span>(555) 014 220 318</span>
      </li>
      <li>
        <svg viewBox="0 0 18 18" aria-label="Mobile"><rect x="5" y="1.5" width="8" height="15" rx="1.5" fill="none" stroke="var(--orange)" stroke-width="2"/><rect x="6.5" y="4" width="5" height="6" fill="var(--orange)"/></svg>
        <span>(555) 014 220 318</span>
      </li>
    </ul>
  </section>

</main>
</body>
</html>
```